Billboard design - consider what a billboard is

Design a billboard using my logo - Billboard is 6m x 3m
A Billboard is advertising for my company that is on a big sign.

Has to be clean and easy to read, and ideally highlights that we are Residential and Commercial builders.

Keep it clean and easy to read

The contact number for the board is

022 583 7092
www.harbourframeworks.co.nz
info@harbourframeworks.co.nz

Doesnt have to have all contact details if it doesnt fit

Has to catch peoples attention to contact us if they need a builder

Can you please change the sign to be all white writing, with black background ?
Updates

Please consider what a billboard is...

The design needs to be suitable for a billboard..

Target Market(s)

people driving past

Industry/Entity Type

Construction

Logo Text

Wellington Builder, website email address, contact number

Colors
0054AA
0677BA
7BADD7
CADEEF
E8F1F8

Requirements
Must have
• Easy to read
Nice to have
• easy to read, can clearly see contact details

```html
<!DOCTYPE html>
<html lang="en">
<head>
<meta charset="utf-8">
<title>Harbour Frameworks – Billboard</title>
<link rel="stylesheet" href="https://fonts.googleapis.com/css2?family=Quicksand:wght@600;700&display=swap">
<style>
  :root {
    --brand-blue: #5e8ac5;
    --brand-grey: #666666;
    --paper: #ffffff;
  }
  html, body {
    margin: 0;
    padding: 0;
    overflow: hidden;
    background: var(--paper);
  }
  .billboard {
    position: relative;
    width: 1200px;
    height: 619px;
    overflow: hidden;
    background: var(--paper);
    font-family: "Quicksand", sans-serif;
  }
  .billboard__shapes {
    position: absolute;
    inset: 0;
  }
  .brand {
    position: absolute;
    left: 95px;
    top: 95px;
    display: flex;
    align-items: center;
    gap: 28px;
  }
  .brand__mark {
    width: 46px;
    height: 46px;
    background: var(--brand-blue);
  }
  .brand__name {
    margin: 0;
    color: var(--brand-blue);
    font-weight: 700;
    font-size: 108px;
    line-height: 0.98;
    letter-spacing: -1px;
  }
  .contact {
    position: absolute;
    left: 0;
    width: 745px;
    top: 424px;
    text-align: center;
    font-weight: 700;
  }
  .contact p { margin: 0; }
  .contact__phone {
    color: var(--brand-blue);
    font-size: 47px;
    line-height: 60px;
  }
  .contact__web {
    color: var(--brand-blue);
    font-size: 35px;
    line-height: 44px;
  }
  .contact__email {
    color: var(--brand-grey);
    font-size: 35px;
    line-height: 44px;
  }
</style>
</head>
<body>
  <main class="billboard">
    <svg class="billboard__shapes" width="1200" height="619" viewBox="0 0 1200 619" aria-hidden="true">
      <circle class="shape-grey-top" cx="980" cy="-80" r="281" fill="var(--brand-grey)"/>
      <circle class="shape-grey-bottom" cx="1000" cy="645" r="272" fill="var(--brand-grey)"/>
      <circle class="shape-blue" cx="1210" cy="270" r="320" fill="var(--brand-blue)"/>
    </svg>

    <div class="brand">
      <span class="brand__mark"></span>
      <h1 class="brand__name">Harbour<br>Frameworks</h1>
    </div>

    <section class="contact">
      <p class="contact__phone">022 583 7092</p>
      <p class="contact__web">www.harbourframeworks.co.nz</p>
      <p class="contact__email">info@harbourframeworks.co.nz</p>
    </section>
  </main>
</body>
</html>
```